Kalvendor Whitmane & Associates

We would like a simple, professional business card using a similar font to our logo.

Industry/Entity Type

Law Firm

Contact Information for Business Card

Martin Kalvendor, Esq. 48 Fennimore Lane, 2nd Floor Brackton, ME 04173 Office: 555.216.4093 Cell: 555.370.8154 Email: marty@kwlawfirm.example kalvendorwhitmanelaw.example

Font styles to use
Other font styles liked:
• We would like to use the fonts used in the logo or similar

Colors
0054AA
0677BA
7BADD7
CADEEF
E8F1F8

Requirements
Must have
• We would like the fonts to match the logo
Nice to have
• not too much design- very simple and professional business card. I added a picture of a business card that I tried to start but I am not a designer! Hopefully it will help with the address and phone numbers and kind of what we are looking for.

```html
<!DOCTYPE html>
<html lang="en">
<head>
<meta charset="utf-8">
<title>Kalvendor Whitmane &amp; Associates – Business Card</title>
<link href="https://fonts.googleapis.com/css2?family=Cinzel:wght@500&family=Roboto:wght@400&display=swap" rel="stylesheet">
<style>
  :root {
    --navy: #1d3a80;
    --ink: #4a4a4a;
    --divider: #6a6a6a;
    --paper: #fbfbfb;
    --backdrop: #9a9a9a;
  }
  * { box-sizing: border-box; margin: 0; padding: 0; }
  html, body { width: 1200px; height: 1050px; overflow: hidden; }
  body {
    background: var(--backdrop);
    display: flex;
    align-items: center;
    justify-content: center;
    gap: 60px;
    font-family: "Roboto", Arial, sans-serif;
  }
  .card {
    background: var(--paper);
    border-bottom: 4px solid var(--navy);
    box-shadow: 0 14px 30px rgba(0,0,0,.25);
  }
  /* contact side (portrait) */
  .card--contact {
    width: 340px;
    height: 595px;
    display: flex;
    flex-direction: column;
    align-items: center;
    padding-top: 120px;
    text-align: center;
  }
  .brand-small {
    display: flex;
    align-items: center;
    gap: 10px;
    color: var(--navy);
    font-family: "Cinzel", Georgia, serif;
    font-weight: 500;
    font-size: 13px;
    letter-spacing: 1px;
  }
  .brand-small .mark { width: 14px; height: 14px; background: var(--navy); flex: none; }
  .person-name {
    margin-top: 34px;
    font-family: "Cinzel", Georgia, serif;
    font-weight: 500;
    font-size: 26px;
    color: var(--navy);
    letter-spacing: 1px;
  }
  .name-rule { width: 60px; height: 2px; background: var(--navy); margin: 14px 0 16px; }
  .address { font-size: 15px; line-height: 1.55; color: var(--ink); }
  .icons { display: flex; gap: 8px; margin-top: 34px; }
  .icons svg { width: 22px; height: 22px; display: block; }
  .contacts { margin-top: 18px; font-size: 15px; line-height: 1.7; color: var(--ink); }
  /* logo side (landscape) */
  .card--brand {
    width: 595px;
    height: 340px;
    display: flex;
    align-items: center;
    justify-content: center;
  }
  .brand-large { display: flex; align-items: center; gap: 22px; }
  .brand-large .mark { width: 44px; height: 44px; background: var(--navy); flex: none; }
  .brand-large .divider { width: 2px; height: 110px; background: var(--divider); flex: none; }
  .brand-large .firm {
    font-family: "Cinzel", Georgia, serif;
    font-weight: 500;
    font-size: 30px;
    line-height: 1.05;
    color: var(--navy);
    letter-spacing: 1px;
  }
</style>
</head>
<body>
  <section class="card card--contact">
    <div class="brand-small"><span class="mark"></span>Kalvendor Whitmane &amp; Associates</div>
    <h1 class="person-name">Martin Kalvendor</h1>
    <div class="name-rule"></div>
    <p class="address">Esq. 48 Fennimore Lane<br>2nd Floor<br>Brackton, ME 04173</p>
    <div class="icons">
      <svg viewBox="0 0 22 22" role="img" aria-label="Office phone"><rect width="22" height="22" fill="var(--navy)"/><path d="M7 5l2.5 0 1 3-1.5 1a7 7 0 0 0 3.5 3.5l1-1.5 3 1v2.5A1.5 1.5 0 0 1 15 16 9 9 0 0 1 6 7 1.5 1.5 0 0 1 7 5z" fill="#fff"/></svg>
      <svg viewBox="0 0 22 22" role="img" aria-label="Cell phone"><rect width="22" height="22" fill="var(--navy)"/><rect x="7.5" y="4.5" width="7" height="13" rx="1" fill="none" stroke="#fff" stroke-width="1.5"/><circle cx="11" cy="15.3" r=".8" fill="#fff"/></svg>
      <svg viewBox="0 0 22 22" role="img" aria-label="Email"><rect width="22" height="22" fill="var(--navy)"/><rect x="5" y="7" width="12" height="8" fill="none" stroke="#fff" stroke-width="1.4"/><path d="M5 7l6 5 6-5" fill="none" stroke="#fff" stroke-width="1.4"/></svg>
      <svg viewBox="0 0 22 22" role="img" aria-label="Website"><rect width="22" height="22" fill="var(--navy)"/><circle cx="11" cy="11" r="5.5" fill="none" stroke="#fff" stroke-width="1.3"/><path d="M5.5 11h11M11 5.5c-2.5 3-2.5 8 0 11M11 5.5c2.5 3 2.5 8 0 11" fill="none" stroke="#fff" stroke-width="1"/></svg>
    </div>
    <p class="contacts">555.216.4093<br>555.370.8154<br>marty@kwlawfirm.example<br>kalvendorwhitmanelaw.example</p>
  </section>

  <section class="card card--brand">
    <div class="brand-large">
      <span class="mark"></span>
      <span class="divider"></span>
      <div class="firm">Kalvendor<br>Whitmane<br>&amp; Associates</div>
    </div>
  </section>
</body>
</html>
```